Postcard Design

I am in real estate, I wish to design a "farming" tool.

I want to show a sampling of houses (files attached) with the following text:

The spring market is here and the buyers are waiting for YOU!
Order a Market Snapshot to see what homes in your neighborhood are selling for, or call today for a personal market analysis.

Order your report at: www.48213HouseDeals.com
or reach out to me directly:
Dana Pelworth
www.SettleinBrambury.com
614.382.7095
YourRealtorDana@Mailvex.com

I also attached multiple files containing logos - in multiple formats and in black or white, depending on what is easier to use.

Target Market(s)

By neighborhood. I have a list.

Industry/Entity Type

Real Estate

Requirements
Must have
• See description above

```html
<!DOCTYPE html>
<html lang="en">
<head>
<meta charset="utf-8">
<title>Spring Market Postcard</title>
<link href="https://fonts.googleapis.com/css2?family=Oswald:wght@600&family=Open+Sans:wght@400;600;700&display=swap" rel="stylesheet">
<style>
  :root {
    --backdrop: #e6e6e6;
    --forest: #1f4d2b;
    --leaf: #b7dd8f;
    --paper: #ffffff;
    --ink: #1c1c1c;
    --bar: #2b2b2b;
    --sky: #aac6e4;
    --lawn: #6f9a4c;
    --siding: #b9ad98;
  }
  * { box-sizing: border-box; margin: 0; padding: 0; }
  html, body { width: 1200px; height: 891px; overflow: hidden; }
  body { background: var(--backdrop); position: relative; font-family: "Open Sans", sans-serif; }

  .postcard { position: absolute; top: 163px; height: 273px; background: var(--paper); overflow: hidden; }

  /* Front */
  .postcard--front { left: 217px; width: 359px; background: var(--forest); }
  .front__headline {
    height: 36px; display: flex; align-items: center; justify-content: center;
    font-family: "Oswald", sans-serif; font-weight: 600; font-size: 11.5px; color: var(--paper);
  }
  .front__hero {
    position: absolute; left: 0; top: 36px; width: 258px; height: 193px;
    background: linear-gradient(180deg, var(--sky) 0%, #d8e4ee 30%, var(--siding) 45%, #a79a84 72%, var(--lawn) 86%, #5d8a3d 100%);
  }
  .front__thumbs { position: absolute; left: 263px; top: 39px; width: 93px; display: flex; flex-direction: column; gap: 4px; }
  .front__thumb { height: 60px; background: linear-gradient(180deg, #c9d9e9 0%, #9c9486 50%, #6e8f52 100%); }
  .front__footer { position: absolute; left: 0; top: 229px; width: 100%; height: 44px; }
  .front__agent {
    position: absolute; left: 12px; top: 9px;
    font-weight: 600; color: var(--paper); line-height: 1.15; white-space: nowrap;
  }
  .front__agent .agent__name { font-size: 15px; }
  .front__agent .agent__firm { font-size: 8px; letter-spacing: 1.5px; text-transform: uppercase; }
  .front__contacts { position: absolute; left: 214px; top: 5px; }

  .contact-list { list-style: none; }
  .contact-list li { display: flex; align-items: center; gap: 5px; line-height: 1; }
  .contact-list svg { flex: none; }
  .contact-list--light li { color: var(--paper); font-size: 7.5px; margin-bottom: 3px; }
  .contact-list--light li.phone { font-size: 10px; font-weight: 600; }

  /* Back */
  .postcard--back { left: 653px; width: 363px; }
  .back__message {
    position: absolute; left: 30px; top: 15px; width: 302px; height: 72px;
    background: var(--forest); text-align: center; padding-top: 6px;
  }
  .back__headline { font-weight: 700; font-size: 10.5px; color: var(--leaf); }
  .back__body { font-size: 9.2px; color: var(--paper); line-height: 1.3; margin: 5px 34px 0; }
  .back__contacts { position: absolute; left: 128px; top: 106px; }
  .contact-list--dark li { color: var(--ink); font-size: 7.5px; margin-bottom: 3px; }
  .contact-list--dark li.phone { font-size: 10px; font-weight: 600; }
  .back__brand { position: absolute; left: 8px; top: 148px; display: flex; align-items: center; gap: 8px; }
  .brand__square { width: 44px; height: 44px; background: var(--forest); }
  .brand__text { font-weight: 600; color: var(--ink); line-height: 1.15; }
  .brand__name { font-size: 19px; }
  .brand__firm { font-size: 8px; letter-spacing: 1.5px; text-transform: uppercase; }
  .back__address-label { position: absolute; left: 177px; top: 193px; font-weight: 700; font-size: 9px; color: var(--ink); }
  .back__address { position: absolute; left: 210px; top: 208px; font-size: 8.5px; color: var(--ink); }
  .back__order {
    position: absolute; left: 5px; top: 223px; width: 355px; height: 30px;
    background: var(--bar); color: var(--paper); font-weight: 600; font-size: 11px;
    display: flex; align-items: center; justify-content: center;
  }
  .back__note { position: absolute; left: 0; top: 259px; width: 100%; text-align: center; font-weight: 700; font-size: 7.5px; color: var(--ink); }
</style>
</head>
<body>

<section class="postcard postcard--front">
  <h1 class="front__headline">The spring market is here and the buyers are waiting for YOU!</h1>
  <div class="front__hero" role="img" aria-label="Photo of a two-storey suburban house with garage and front lawn"></div>
  <div class="front__thumbs">
    <div class="front__thumb" role="img" aria-label="Photo of a brick colonial house"></div>
    <div class="front__thumb" role="img" aria-label="Photo of a grey two-storey house"></div>
    <div class="front__thumb" role="img" aria-label="Photo of a split-level house with garden"></div>
  </div>
  <footer class="front__footer">
    <div class="front__agent">
      <div class="agent__name">Dana Pelworth</div>
      <div class="agent__firm">Ridgeline Realty</div>
    </div>
    <ul class="contact-list contact-list--light front__contacts">
      <li class="phone"><svg width="9" height="9" viewBox="0 0 10 10"><circle cx="5" cy="5" r="5" fill="#b7dd8f"/><path d="M3 2.5l1.2 1.2-.6.8a4 4 0 0 0 1.9 1.9l.8-.6L7.5 7 6.8 7.8C4.6 7.6 2.4 5.4 2.2 3.2z" fill="#1f4d2b"/></svg>614.382.7095</li>
      <li><svg width="9" height="9" viewBox="0 0 10 10"><circle cx="5" cy="5" r="5" fill="#b7dd8f"/><circle cx="5" cy="5" r="2.6" fill="none" stroke="#1f4d2b" stroke-width=".8"/><path d="M2.4 5h5.2M5 2.4v5.2" stroke="#1f4d2b" stroke-width=".7"/></svg>www.SettleinBrambury.com</li>
      <li><svg width="9" height="9" viewBox="0 0 10 10"><circle cx="5" cy="5" r="5" fill="#b7dd8f"/><rect x="2.5" y="3.3" width="5" height="3.4" fill="none" stroke="#1f4d2b" stroke-width=".7"/><path d="M2.5 3.3L5 5.3l2.5-2" fill="none" stroke="#1f4d2b" stroke-width=".7"/></svg>YourRealtorDana@Mailvex.com</li>
    </ul>
  </footer>
</section>

<section class="postcard postcard--back">
  <div class="back__message">
    <h2 class="back__headline">The spring is here and the buyers are waiting for YOU!</h2>
    <p class="back__body">Order a Market Snapshot to see what homes in your neighborhood are selling for, or call today for a personal market analysis.</p>
  </div>
  <ul class="contact-list contact-list--dark back__contacts">
    <li class="phone"><svg width="9" height="9" viewBox="0 0 10 10"><circle cx="5" cy="5" r="5" fill="#b7dd8f"/><path d="M3 2.5l1.2 1.2-.6.8a4 4 0 0 0 1.9 1.9l.8-.6L7.5 7 6.8 7.8C4.6 7.6 2.4 5.4 2.2 3.2z" fill="#1f4d2b"/></svg>614.382.7095</li>
    <li><svg width="9" height="9" viewBox="0 0 10 10"><circle cx="5" cy="5" r="5" fill="#b7dd8f"/><circle cx="5" cy="5" r="2.6" fill="none" stroke="#1f4d2b" stroke-width=".8"/><path d="M2.4 5h5.2M5 2.4v5.2" stroke="#1f4d2b" stroke-width=".7"/></svg>www.SettleinBrambury.com</li>
    <li><svg width="9" height="9" viewBox="0 0 10 10"><circle cx="5" cy="5" r="5" fill="#b7dd8f"/><rect x="2.5" y="3.3" width="5" height="3.4" fill="none" stroke="#1f4d2b" stroke-width=".7"/><path d="M2.5 3.3L5 5.3l2.5-2" fill="none" stroke="#1f4d2b" stroke-width=".7"/></svg>YourRealtorDana@Mailvex.com</li>
  </ul>
  <div class="back__brand">
    <div class="brand__square"></div>
    <div class="brand__text">
      <div class="brand__name">Dana Pelworth</div>
      <div class="brand__firm">Ridgeline Realty</div>
    </div>
  </div>
  <div class="back__address-label">Address:</div>
  <div class="back__address">Brambury County, OH 43218</div>
  <div class="back__order">Order your report at: www.48213HouseDeals.com</div>
  <div class="back__note">See description above</div>
</section>

</body>
</html>
```